Business card for apparel company. Specializing in fishing and boating performance wear. Main company name is Marlow Pelican Company, LLC brand name for apparel is TIDEWAKE. See website www.TidewakeBayline.com I will attach some logos to consider.

```html
<!DOCTYPE html>
<html lang="en">
<head>
<meta charset="utf-8">
<title>Tidewake Business Card</title>
<link rel="stylesheet" href="https://fonts.googleapis.com/css2?family=Lato:wght@400;700;900&display=swap">
<style>
  :root {
    --bg: #3f454d;
    --card: #ffffff;
    --brand-blue: #0a86dc;
    --deep-blue: #0b5cc2;
    --sky-blue: #25a0e8;
    --ocean-dark: #0a4ea6;
    --ocean-light: #1f86d8;
    --accent-orange: #e2642a;
    --white: #ffffff;
  }
  * { box-sizing: border-box; margin: 0; padding: 0; }
  html, body {
    width: 1200px; height: 875px; overflow: hidden;
    background: var(--bg);
    font-family: "Lato", sans-serif;
  }
  .stage {
    width: 1200px; height: 875px;
    display: flex; align-items: center; justify-content: center; gap: 40px;
  }
  .card {
    position: relative;
    width: 540px; height: 309px;
    background: var(--card);
    border-radius: 18px;
    overflow: hidden;
  }
  .brand {
    display: flex; align-items: center; gap: 14px;
    color: var(--brand-blue);
    font-weight: 900;
    letter-spacing: 2px;
    white-space: nowrap;
  }
  .brand-dot {
    border-radius: 50%;
    background: var(--brand-blue);
    flex: none;
  }
  .card-front .brand {
    position: absolute; inset: 0;
    justify-content: center;
    font-size: 64px;
  }
  .card-front .brand-dot { width: 34px; height: 34px; }

  .card-back .wave { position: absolute; inset: 0; }
  .card-back .brand {
    position: absolute; left: 32px; top: 104px;
    font-size: 34px; gap: 9px; letter-spacing: 1.5px;
  }
  .card-back .brand-dot { width: 20px; height: 20px; }
  .person {
    position: absolute; right: 36px; top: 18px;
    text-align: right;
  }
  .person-name {
    color: var(--deep-blue);
    font-weight: 900; font-size: 24px; letter-spacing: 0.5px;
  }
  .person-title {
    color: var(--sky-blue);
    font-size: 15px; margin-top: 1px;
  }
  .contact {
    position: absolute; right: 24px; top: 162px;
    list-style: none;
    color: var(--white);
    text-align: right;
    font-size: 12.5px; line-height: 1.7;
    white-space: nowrap;
  }
  .contact li { display: flex; justify-content: flex-end; align-items: center; gap: 8px; }
  .contact .company { font-weight: 700; font-size: 13.5px; }
  .contact svg { width: 12px; height: 12px; flex: none; }
  .contact .spacer { width: 12px; flex: none; }
</style>
</head>
<body>
<main class="stage">
  <section class="card card-front">
    <div class="brand"><span class="brand-dot"></span>TIDEWAKE</div>
  </section>

  <section class="card card-back">
    <svg class="wave" viewBox="0 0 540 309" width="540" height="309">
      <defs>
        <linearGradient id="ocean" x1="0" y1="1" x2="1" y2="0">
          <stop offset="0" stop-color="var(--ocean-dark)"/>
          <stop offset="1" stop-color="var(--ocean-light)"/>
        </linearGradient>
      </defs>
      <path role="img" aria-label="Underwater ocean photograph with bubbles and reef"
            d="M0,250 C120,290 225,275 272,175 C312,98 400,98 540,98 L540,309 L0,309 Z"
            fill="url(#ocean)"/>
      <path d="M262,172 C302,90 400,86 540,86" fill="none" stroke="var(--deep-blue)" stroke-width="5"/>
      <path d="M18,238 C130,270 222,256 262,188" fill="none" stroke="var(--accent-orange)" stroke-width="3"/>
    </svg>

    <div class="person">
      <div class="person-name">EVAN CALDER</div>
      <div class="person-title">Founder &amp; CEO</div>
    </div>

    <div class="brand"><span class="brand-dot"></span>TIDEWAKE</div>

    <ul class="contact">
      <li class="company">Marlow Pelican Company, LLC
        <svg viewBox="0 0 12 12"><path d="M6 0.5a4 4 0 0 1 4 4c0 3-4 7-4 7s-4-4-4-7a4 4 0 0 1 4-4z" fill="#fff"/><circle cx="6" cy="4.5" r="1.5" fill="var(--ocean-light)"/></svg>
      </li>
      <li>P.O. Box 418, Gullport, Florida 34720<span class="spacer"></span></li>
      <li>info@MarlowPelicanCo.com
        <svg viewBox="0 0 12 12"><rect x="0.5" y="2.5" width="11" height="7" rx="1" fill="#fff"/><path d="M1 3l5 3.5L11 3" fill="none" stroke="var(--ocean-light)" stroke-width="1"/></svg>
      </li>
      <li>www.TidewakeBayline.com
        <svg viewBox="0 0 12 12"><circle cx="6" cy="6" r="5.5" fill="#fff"/><path d="M0.5 6h11M6 0.5c-2.5 3-2.5 8 0 11M6 0.5c2.5 3 2.5 8 0 11" fill="none" stroke="var(--ocean-light)" stroke-width="0.9"/></svg>
      </li>
    </ul>
  </section>
</main>
</body>
</html>
```